Website Design For Ecommerce Brand That Sells Personalized Wall Decor

We need a new website for our company Copper Lantern. Our current site is functioning through wordpress/woocomerce but we are not happy with the appearance. Our products really wow people when they receive them and we need your help making our website do the same!

Number of Pages Required

4 page

```html
<!DOCTYPE html>
<html lang="en">
<head>
<meta charset="utf-8">
<title>Copper Lantern — Personalized Wall Decor</title>
<link href="https://fonts.googleapis.com/css2?family=Poppins:wght@300;400;500;600&family=Great+Vibes&family=Playfair+Display:ital@1&display=swap" rel="stylesheet">
<style>
:root{
  --orange:#e8834a;
  --orange-light:#f0a071;
  --gold:#f5b400;
  --ink:#1e1e1e;
  --muted:#777;
  --line:#e4e4e4;
  --panel:#f6f6f8;
  --footer:#f2f2f4;
  --wood-dark:#4a3a2e;
  --wood-mid:#8a7360;
  --wood-light:#d9c8b2;
}
*{margin:0;padding:0;box-sizing:border-box}
html,body{width:1200px;height:4147px;overflow:hidden;background:#fff}
body{font-family:'Poppins',sans-serif;color:var(--ink);position:relative}
.abs{position:absolute}
.script{font-family:'Great Vibes',cursive;color:var(--orange);font-weight:400}
.serif-btn{font-family:'Playfair Display',serif;font-style:italic}

/* top bar */
.topbar{left:60px;right:60px;top:0;height:36px;border-bottom:1px solid var(--line);font-size:12px;color:var(--muted);display:flex;justify-content:space-between;align-items:center}
.topbar b{color:var(--ink);font-weight:500}

/* header */
.search{left:60px;top:72px;width:170px;border-bottom:1px solid #bbb;height:20px;font-size:11px;color:#555;text-align:right;padding-right:0}
.search svg{position:absolute;left:0;top:6px}
.brand{left:0;right:0;top:56px;text-align:center}
.brand-name{display:inline-flex;align-items:center;gap:8px;font-size:20px;font-weight:500;letter-spacing:2px}
.brand-name i{width:14px;height:14px;background:var(--ink);border-radius:50%;display:inline-block}
.locale{left:860px;top:76px;font-size:11px;color:#888;display:flex;gap:20px}
.icons{left:1030px;top:74px;display:flex;gap:24px}
.nav{left:0;right:0;top:148px;text-align:center;font-size:12px;letter-spacing:2px;font-weight:500}
.nav span{margin:0 18px}
.header-line{left:0;right:0;top:182px;border-top:1px solid var(--line)}

/* hero */
.hero{left:0;width:1200px;display:flex;flex-direction:column;align-items:center;justify-content:center;color:#fff;text-align:center}
.hero h1{font-size:40px;font-weight:500;letter-spacing:6px;line-height:1}
.hero .script{font-size:44px;color:#f4a55a;margin-bottom:-20px;position:relative}
.hero p{font-size:12px;max-width:420px;margin-top:14px;line-height:1.4}
.hero .btn{margin-top:22px;border:1px solid #fff;width:140px;height:38px;line-height:38px;font-size:14px;letter-spacing:2px}
.dots{display:flex;gap:22px;align-items:center;justify-content:center}
.dots i{width:6px;height:6px;border-radius:50%;background:#fff;display:block}
.dots i.on{width:20px;height:20px;border:1px solid #fff;background:transparent;position:relative}
.dots i.on::after{content:"";position:absolute;left:6px;top:6px;width:6px;height:6px;border-radius:50%;background:#fff}

/* promo */
.promo{top:657px;width:522px;height:247px;overflow:hidden}
.promo .band{position:absolute;left:0;right:0;top:60px;height:64px;display:flex;align-items:center;justify-content:center;color:#fff;font-size:44px;font-style:italic;font-weight:500;letter-spacing:6px}
.promo .sub{position:absolute;left:0;right:0;top:157px;text-align:center;font-family:'Playfair Display',serif;font-style:italic;font-size:13px;letter-spacing:3px;color:#fff}

/* section titles */
.sec-title{left:0;right:0;text-align:center}
.sec-title .script{font-size:30px;display:block;line-height:1}
.sec-title h2{font-size:32px;font-weight:600;letter-spacing:5px;line-height:1}

/* products */
.product{width:251px}
.product .photo{height:211px}
.product .cap{font-size:12.5px;margin-top:12px;line-height:1.4}
.product .price{font-size:12.5px;font-weight:600;margin-top:4px}
.product .price b{color:var(--gold);font-weight:500}
.pdots{display:flex;gap:18px;justify-content:center}
.pdots i{width:10px;height:10px;border-radius:50%;background:#ddd;display:block}
.pdots i.on{background:var(--gold)}

/* welcome */
.welcome-panel{left:333px;top:1477px;width:867px;height:537px;background:var(--panel)}
.welcome-text{left:633px;top:1585px;width:400px}
.welcome-text .script{font-size:32px;line-height:1}
.welcome-text h2{font-size:32px;font-weight:600;letter-spacing:4px;margin-top:2px}
.welcome-text p{font-size:13px;color:#555;line-height:1.45;margin-top:12px}
.outline-btn{width:142px;height:40px;border:1px solid var(--orange);color:var(--orange);text-align:center;line-height:38px;font-size:15px;letter-spacing:2px}

/* latest */
.latest-title{left:60px;top:3090px;font-size:32px;font-weight:600;letter-spacing:5px}

/* partners */
.partner{top:3527px;height:50px;background:#e9e9ec;border-radius:6px}
.partner.round{border-radius:50%;width:60px;height:60px;top:3522px}

/* newsletter */
.newsletter{left:0;top:3633px;width:1200px;height:161px;background:var(--orange)}
.newsletter h3{position:absolute;left:158px;top:66px;color:#fff;font-size:21px;font-weight:600;letter-spacing:0.5px}
.newsletter .field{position:absolute;left:512px;top:59px;width:355px;height:42px;background:var(--orange-light);color:#fbe0cf;font-size:11px;padding-left:22px;line-height:42px}
.newsletter .submit{position:absolute;left:872px;top:59px;width:161px;height:42px;background:#fff;color:var(--orange);font-size:18px;text-align:center;line-height:42px}

/* footer */
.footer{left:0;top:3794px;width:1200px;height:353px;background:var(--footer)}
.fcol{top:79px}
.fcol h4{font-size:16px;font-weight:600;letter-spacing:3px;margin-bottom:18px}
.fcol li{list-style:none;font-size:11px;letter-spacing:1.5px;line-height:25px;color:#333}
.social{display:flex;gap:10px;margin-top:30px}
.social i{width:16px;height:16px;border:1px solid #666;border-radius:50%;display:block}
.copy{left:158px;top:300px;font-size:12px;letter-spacing:1px;color:#444}
.pay{left:826px;top:297px;display:flex;gap:5px}
.pay i{width:21px;height:14px;background:#9a9aa2;border-radius:2px;display:block}
</style>
</head>
<body>

<!-- top bar -->
<div class="abs topbar"><span>Free shipping for orders over $59!</span><span>Email Us At:Support@<b>Copperlantern</b>.Com</span></div>

<!-- header -->
<div class="abs search">SEARCH
  <svg width="13" height="13" viewBox="0 0 13 13"><circle cx="5.5" cy="5.5" r="4.3" fill="none" stroke="#333" stroke-width="1.4"/><line x1="8.7" y1="8.7" x2="12" y2="12" stroke="#333" stroke-width="1.4"/></svg>
</div>
<div class="abs brand"><span class="brand-name"><i></i>COPPER LANTERN</span></div>
<div class="abs locale"><span>ENGLISH ⌵</span><span>USD ⌵</span></div>
<div class="abs icons">
  <svg width="18" height="18" viewBox="0 0 18 18"><circle cx="9" cy="6" r="4" fill="none" stroke="#333" stroke-width="1.4"/><path d="M2 17c0-4 3-6 7-6s7 2 7 6" fill="none" stroke="#333" stroke-width="1.4"/></svg>
  <svg width="18" height="18" viewBox="0 0 18 18"><path d="M9 16L2.5 9.5A3.8 3.8 0 019 4.2a3.8 3.8 0 016.5 5.3z" fill="none" stroke="#333" stroke-width="1.4"/></svg>
  <svg width="20" height="18" viewBox="0 0 20 18"><path d="M3 6h12l-1 11H4z" fill="none" stroke="#333" stroke-width="1.4"/><path d="M6 6a3 3 0 016 0" fill="none" stroke="#333" stroke-width="1.4"/><circle cx="16" cy="3" r="3" fill="var(--orange)"/></svg>
</div>
<div class="abs nav"><span>HOME</span><span>PRODUCTS</span><span>FAQ</span><span>CONTACT US</span></div>
<div class="abs header-line"></div>

<!-- hero -->
<div class="abs" style="left:0;top:184px;width:1200px;height:440px;background:linear-gradient(90deg,#c9ccc4 0%,#8d8f83 30%,#5a4a3e 60%,#3f342c 100%)" role="img" aria-label="Engraved wooden family tree plaque with name-tagged leaves beside a potted fern on a shelf"></div>
<div class="abs hero" style="top:184px;height:440px">
  <span class="script">Authentic</span>
  <h1>MADE WITH LOVE</h1>
  <p>Lorem ipsum dolor sit amet, consectetur adipiscing elit, sed do eiusmod tempor incididunt ut labore et dolor</p>
  <div class="btn serif-btn">Shop Now</div>
  <div class="dots" style="margin-top:48px"><i></i><i class="on"></i><i></i></div>
</div>

<!-- promo banners -->
<div class="abs promo" style="left:60px;background:linear-gradient(135deg,#9a7b62,#c9b7a2 50%,#6d5d4c)" role="img" aria-label="Hand holding a personalized wooden gnome sign">
  <div class="band" style="background:rgba(232,131,74,0.85)">GNOME</div>
  <div class="sub">VIEW COLLECTION</div>
</div>
<div class="abs promo" style="left:619px;background:linear-gradient(135deg,#8a7a6c,#d8ccbc 50%,#a79582)" role="img" aria-label="Layered wooden family tree sign with script lettering">
  <div class="band" style="background:rgba(240,196,40,0.85)">NEW ARRIVALS</div>
  <div class="sub">SHOP NOW</div>
</div>

<!-- personalized family tree -->
<div class="abs sec-title" style="top:952px"><span class="script">Copper Lantern</span><h2>PERSONALIZED<br>FAMILY TREE</h2></div>

<div class="abs product" style="left:60px;top:1084px"><div class="photo" style="background:linear-gradient(135deg,#5b3f2c,#c9a884 50%,#4a3222)" role="img" aria-label="Wooden name ornament with dinosaur cutout on dark wood"></div><div class="cap">12 Inch Square<br>Framed Personalized Family Tree...</div><div class="price">FROM <b>$69.00</b></div></div>
<div class="abs product" style="left:337px;top:1084px"><div class="photo" style="background:radial-gradient(circle,#cfc3b4,#5a4838 70%)" role="img" aria-label="Round family tree plaque with many heart leaves"></div><div class="cap">12 Inch Square<br>Framed Personalized Family Tree...</div><div class="price">FROM <b>$69.00</b></div></div>
<div class="abs product" style="left:614px;top:1084px"><div class="photo" style="background:linear-gradient(135deg,#f2f0ec,#d8c7ad 55%,#ece8e2)" role="img" aria-label="Layered wooden family sign with tree on white wall"></div><div class="cap">12 Inch Square<br>Framed Personalized Family Tree...</div><div class="price">FROM <b>$69.00</b></div></div>
<div class="abs product" style="left:890px;top:1084px"><div class="photo" style="background:radial-gradient(circle,#cbbfae,#5d4b3b 70%)" role="img" aria-label="Round dark family tree plaque with light leaves"></div><div class="cap">12 Inch Square<br>Framed Personalized Family Tree...</div><div class="price">FROM <b>$69.00</b></div></div>
<div class="abs pdots" style="left:0;right:0;top:1409px"><i></i><i class="on"></i><i></i></div>

<!-- welcome -->
<div class="abs welcome-panel"></div>
<div class="abs" style="left:60px;top:1543px;width:240px;height:384px;background:linear-gradient(160deg,#3f5a3a,#e8d6bf 45%,#b5562f)" role="img" aria-label="Hand holding a wooden pet memorial ornament with paw print"></div>
<div class="abs" style="left:333px;top:1543px;width:241px;height:384px;background:linear-gradient(160deg,#8b2e2a,#d7c2a6 45%,#6a4a36)" role="img" aria-label="Wooden holiday gnome ornament with sign beside red baubles"></div>
<div class="abs welcome-text">
  <span class="script">Welcome to</span>
  <h2>COPPER LANTERN</h2>
  <p>Lorem ipsum dolor sit amet, consectetur adipiscing elit, sed do eiusmod tempor incididunt ut labore et dolore magna aliqua. Ut enim ad minim veniam, quis nostrud exercitation ullamco laboris nisi</p>
  <p>ut aliquip ex ea commodo consequat. Duis aute irure dolor in reprehenderit in voluptate velit esse cillumdolore .eu fugiat nulla pariatur</p>
</div>
<div class="abs outline-btn serif-btn" style="left:636px;top:1849px">Shop Now</div>

<!-- second banner -->
<div class="abs" style="left:0;top:2022px;width:1200px;height:449px;background:linear-gradient(100deg,#3a2d25 0%,#6f5d4f 35%,#4c3d32 70%,#2f261f 100%)" role="img" aria-label="Wooden name ornaments with animal cutouts hanging on twine"></div>
<div class="abs hero" style="top:2022px;height:449px">
  <span class="script">Home Decor</span>
  <h1>ED UT PERSPICIATIS UNDE</h1>
  <p>Lorem ipsum dolor sit amet, consectetur adipiscing elit, sed do eiusmod tempor incididunt ut labore et dolor</p>
  <div class="btn serif-btn">Shop Now</div>
  <div class="dots" style="margin-top:48px"><i></i><i class="on"></i><i></i></div>
</div>

<!-- best selling -->
<div class="abs sec-title" style="top:2518px"><span class="script">Copper Lantern</span><h2>BEST SELLING</h2></div>
<div class="abs product" style="left:60px;top:2619px"><div class="photo" style="background:linear-gradient(160deg,#cfd2d0,#8a6a4c 55%,#5a4030)" role="img" aria-label="Stack of wooden frames in a workshop"></div><div class="cap">12 Inch Square<br>Framed Personalized Family Tree...</div><div class="price">FROM <b>$69.00</b></div></div>
<div class="abs product" style="left:337px;top:2619px"><div class="photo" style="background:linear-gradient(160deg,#3a3634,#c9c2b8 55%,#2f2b29)" role="img" aria-label="Dark campers welcome sign with trees and camper"></div><div class="cap">12 Inch Square<br>Framed Personalized Family Tree...</div><div class="price">FROM <b>$69.00</b></div></div>
<div class="abs product" style="left:614px;top:2619px"><div class="photo" style="background:linear-gradient(160deg,#2d2a28,#b7aa98 50%,#3a3431)" role="img" aria-label="Close-up of layered wooden script lettering"></div><div class="cap">12 Inch Square<br>Framed Personalized Family Tree...</div><div class="price">FROM <b>$69.00</b></div></div>
<div class="abs product" style="left:890px;top:2619px"><div class="photo" style="background:linear-gradient(160deg,#e6e3de,#c9b9a4 60%,#a89884)" role="img" aria-label="Stack of plywood sheets"></div><div class="cap">12 Inch Square<br>Framed Personalized Family Tree...</div><div class="price">FROM <b>$69.00</b></div></div>
<div class="abs pdots" style="left:0;right:0;top:2945px"><i></i><i class="on"></i><i></i></div>

<!-- latest product -->
<div class="abs latest-title">LATEST PRODUCT</div>
<div class="abs product" style="left:60px;top:3154px"><div class="photo" style="background:linear-gradient(135deg,#4a3c30,#b8a080 50%,#3a2e25)" role="img" aria-label="Framed honeycomb and bee wall sign"></div><div class="cap">12 Inch Square<br>Framed Personalized Family Tree...</div><div class="price">FROM <b>$69.00</b></div></div>
<div class="abs product" style="left:337px;top:3154px"><div class="photo" style="background:linear-gradient(135deg,#7a2a22,#c56a3a 45%,#5a3a28)" role="img" aria-label="Round welcome sign with gnome and seasonal pieces"></div><div class="cap">12 Inch Square<br>Framed Personalized Family Tree...</div><div class="price">FROM <b>$69.00</b></div></div>
<div class="abs" style="left:640px;top:3066px;width:560px;height:407px;background:linear-gradient(135deg,#6c7a4a,#3a2e26 40%,#c2b19a 70%,#5e6a40)" role="img" aria-label="Hands holding a framed campers sign with trees, moon and stars outdoors"></div>

<!-- partners -->
<div class="abs partner" style="left:70px;width:125px"></div>
<div class="abs partner round" style="left:256px"></div>
<div class="abs partner" style="left:400px;width:85px"></div>
<div class="abs partner round" style="left:568px"></div>
<div class="abs partner" style="left:705px;width:100px"></div>
<div class="abs partner" style="left:880px;width:125px"></div>
<div class="abs partner round" style="left:1066px"></div>

<!-- newsletter -->
<div class="abs newsletter">
  <h3>SIGN UP OUR NEWSLETTER</h3>
  <div class="field">Enter Your Email</div>
  <div class="submit serif-btn">Submit</div>
</div>

<!-- footer -->
<div class="abs footer">
  <div class="abs fcol" style="left:158px"><h4>CONTACT</h4><ul><li>SUPPORT@COPPERLANTERN.COM</li><li>CEDAR FALLS, FL 34100</li></ul><div class="social"><i></i><i></i><i></i><i></i><i></i></div></div>
  <div class="abs fcol" style="left:428px"><h4>HELP</h4><ul><li>FAQS</li><li>PRICING PLANS</li><li>TRACK</li><li>YOUR ORDER</li><li>MY ACCOUNT</li></ul></div>
  <div class="abs fcol" style="left:602px"><h4>ABOUT US</h4><ul><li>OUR STORY</li><li>JOB OPPORTUNITIES</li><li>STORE LOCATOR</li><li>CONTACT US</li></ul></div>
  <div class="abs fcol" style="left:817px"><h4>CUSTOMER SERVICE</h4><ul><li>MY ACCOUNT</li><li>TERMS OF USE</li><li>DELIVERIES &amp; RETURNS</li><li>GIFT CARD</li></ul></div>
  <div class="abs copy">Copyright © 2022 Copperlantern. All Rights Reserved</div>
  <div class="abs pay"><i></i><i></i><i></i><i></i><i></i><i></i></div>
</div>

</body>
</html>
```